Young judge needs a website to publish and to connect

I would like to have a website where I can publish my articles in public law. I am judge at the Alpine Civic Appeals Chamber. Therefore, the website must have a calm, friendly and fairly neutral design. Also, it should be mobile friendly and easy to use.

On my website, I want to

- publish articles such as https://www.quorvely.com/notes/how-win-court-tobias-wrenholt/ and get feedbacks from my colleagues
- generate interest for my project on 'Rules and Ballots - Notes from the Dais', a book that I would like to publish in 2020 and which brings together my publications on public law (http://www.statutewell.ch/content/english/profil/publikationen.html ).
- provide updates for my university courses on constitutional, administrative and international law.

For that purpose, I would kindly ask you to suggest a website that communicates a fresh approach to the work of a young judge in constitutional and administrative law. Please have in mind that I do not only sit on the bench, but that I also work in academia. Therefore, it should be suitable for an audience from both university and law practice. The website should replace the existing website on www.statutewell.ch that I designed when still working as a lawyer. Thank you.

Target Market(s)

Academica, law firms, courts

Industry/Entity Type

University

Contact Information for Business Card

Tobias Wrenholt
Judge
Alpine Civic Appeals Chamber
M +41 78 5XX 9X 2X

Logo Text

Notes from the Dais

Number of Pages Required

5+ page

Font styles to use
Sans Serif

Colors
0455a3

Requirements
Must have
• - a page where I can publish and get feedbacks
• - a page about my project on law and politics
• - a page where I can provide updates for my university courses on constitutional, administrative and international law
• - page where I can list current and planned projects
• - a collaborative, young and fresh approach
Nice to have
• - a page reserved for my colleagues at the Alpine Civic Appeals Chamber where I can alert them about to possibility to collaborate (if possibly password protected) and where they may suggest what to contribute to a specific project
Should not have
• anything which might to suggest that I want to make money with it, bragging or pretentious. Do not forget: I am judge, not a barrister.

```html
<!DOCTYPE html>
<html lang="en">
<head>
<meta charset="utf-8">
<title>Publications – Tobias Wrenholt</title>
<link href="https://fonts.googleapis.com/css2?family=Lato:wght@400;700;900&family=Open+Sans:wght@300;400&display=swap" rel="stylesheet">
<style>
  :root {
    --ink: #111111;
    --header-bg: #141414;
    --footer-bg: #000000;
    --accent: #1a78c8;
    --brand: #0455a3;
    --white: #ffffff;
    --body-text: #3a3a3a;
    --social: #1a8ed0;
  }
  * { margin: 0; padding: 0; box-sizing: border-box; }
  html, body { width: 960px; height: 1200px; overflow: hidden; background: var(--white); }
  body { position: relative; font-family: "Lato", sans-serif; color: var(--ink); }

  .site-header {
    position: absolute; left: 0; top: 0; width: 960px; height: 95px;
    background: var(--header-bg); border-bottom: 1px solid #3a3a3a;
  }
  .nav-link {
    position: absolute; top: 43px; color: var(--white);
    font-size: 16px; letter-spacing: 0.2px; text-decoration: none;
  }
  .brand {
    position: absolute; left: 380px; top: 20px; width: 194px; text-align: center;
    display: flex; align-items: center; justify-content: center; gap: 8px;
  }
  .brand-mark { width: 12px; height: 12px; background: var(--brand); }
  .brand-name { color: var(--white); font-size: 20px; font-weight: 400; line-height: 1.2; }

  .hero {
    position: absolute; left: 0; top: 96px; width: 960px; height: 276px;
    background: linear-gradient(90deg, #1a2236 0%, #25301c 12%, #2a2a2a 22%, #3a3016 32%, #3a2a14 42%, #3a1616 52%, #3a3014 62%, #1e3a1c 72%, #2a2c1a 82%, #3a2a10 100%);
  }
  .hero::after {
    content: ""; position: absolute; inset: 0;
    background: linear-gradient(180deg, rgba(0,0,0,0.45) 0%, rgba(0,0,0,0.25) 45%, rgba(0,0,0,0.55) 100%);
  }
  .hero-title {
    position: absolute; left: 0; top: 66px; width: 952px; text-align: center; z-index: 1;
    color: var(--white); font-size: 65px; font-weight: 400; letter-spacing: 1px; line-height: 1;
  }
  .hero-rule {
    position: absolute; left: 232px; top: 147px; width: 476px; height: 3px;
    background: var(--accent); z-index: 1;
  }

  .publication { position: absolute; left: 99px; width: 760px; height: 175px; }
  .pub-image {
    position: absolute; left: 0; top: 0; width: 202px; height: 174px;
    background: radial-gradient(ellipse at 55% 40%, #6a4a34 0%, #3e2a1e 55%, #2a1c14 100%);
  }
  .pub-image.is-active {
    background: linear-gradient(160deg, #5f9bc9 0%, #4a86bb 55%, #3d6fa0 100%);
    display: flex; align-items: center; justify-content: center;
  }
  .read-more { color: var(--white); font-family: "Open Sans", sans-serif; font-size: 19px; }
  .pub-title {
    position: absolute; left: 222px; top: -6px;
    font-size: 33px; font-weight: 900; letter-spacing: 2.4px; line-height: 1.2;
  }
  .pub-excerpt {
    position: absolute; left: 222px; top: 43px; width: 540px;
    font-family: "Open Sans", sans-serif; font-size: 13.6px; line-height: 15.6px;
    color: var(--body-text);
  }
  .pub-rule {
    position: absolute; left: 202px; top: 129px; width: 555px; height: 2px; background: var(--accent);
  }

  .load-more {
    position: absolute; left: 0; top: 1053px; width: 960px; text-align: center;
    font-size: 22px; font-weight: 700; letter-spacing: 0.3px;
  }
  .load-more svg { position: absolute; left: 465px; top: 30px; }

  .site-footer {
    position: absolute; left: 0; top: 1125px; width: 960px; height: 75px; background: var(--footer-bg);
  }
  .copyright {
    position: absolute; left: 0; top: 24px; width: 945px; text-align: center;
    color: var(--white); font-size: 21px; font-weight: 700;
  }
  .social { position: absolute; top: 20px; display: flex; align-items: center; gap: 4px; }
  .social-dot { width: 12px; height: 12px; border-radius: 50%; background: var(--social); }
  .social-name { color: var(--white); font-size: 11px; }
</style>
</head>
<body>
  <header class="site-header">
    <a class="nav-link" style="left:29px" href="#">PROFILE</a>
    <a class="nav-link" style="left:125px" href="#">PROJECTS</a>
    <a class="nav-link" style="left:241px;top:42px" href="#">PUBLICATIONS</a>
    <div class="brand"><span class="brand-mark"></span><span class="brand-name">Tobias Wrenholt</span></div>
    <a class="nav-link" style="left:601px;top:42px" href="#">COURSES</a>
    <a class="nav-link" style="left:712px;top:42px" href="#">COLLABORATE</a>
    <a class="nav-link" style="left:858px;top:41px" href="#">CONTACT</a>
  </header>

  <section class="hero" role="img" aria-label="Row of leather-bound book spines on a library shelf">
    <h1 class="hero-title">PUBLICATIONS</h1>
    <div class="hero-rule"></div>
  </section>

  <article class="publication" style="top:436px">
    <div class="pub-image is-active" role="img" aria-label="Wooden judge's gavel on its block"><span class="read-more">Read More</span></div>
    <h2 class="pub-title">PUBLIC LAW</h2>
    <p class="pub-excerpt">Lorem ipsum dolor sit amet, consectetur adipiscing elit, sed do<br>eiusmod tempor incididunt ut labore et dolore magna aliqua.<br>Ut enim ad minim veniam, quis nostrud exercitation ullamco laboris<br>nisi aliquip ex ea commodo consequat. Duis aute irure dolor in reprehenderit<br>cupidatat non proident, sunt in culpa qui officia deserunt mollit anim id est laborum.</p>
    <div class="pub-rule"></div>
  </article>

  <article class="publication" style="top:644px">
    <div class="pub-image" role="img" aria-label="Wooden judge's gavel on its block"></div>
    <h2 class="pub-title">PUBLIC LAW</h2>
    <p class="pub-excerpt">Lorem ipsum dolor sit amet, consectetur adipiscing elit, sed do<br>eiusmod tempor incididunt ut labore et dolore magna aliqua.<br>Ut enim ad minim veniam, quis nostrud exercitation ullamco laboris<br>nisi aliquip ex ea commodo consequat. Duis aute irure dolor in reprehenderit<br>cupidatat non proident, sunt in culpa qui officia deserunt mollit anim id est laborum.</p>
    <div class="pub-rule" style="top:131px;width:557px"></div>
  </article>

  <article class="publication" style="top:855px">
    <div class="pub-image" role="img" aria-label="Wooden judge's gavel on its block"></div>
    <h2 class="pub-title">PUBLIC LAW</h2>
    <p class="pub-excerpt">Lorem ipsum dolor sit amet, consectetur adipiscing elit, sed do<br>eiusmod tempor incididunt ut labore et dolore magna aliqua.<br>Ut enim ad minim veniam, quis nostrud exercitation ullamco laboris<br>nisi aliquip ex ea commodo consequat. Duis aute irure dolor in reprehenderit<br>cupidatat non proident, sunt in culpa qui officia deserunt mollit anim id est laborum.</p>
    <div class="pub-rule" style="top:132px"></div>
  </article>

  <div class="load-more">LOAD MORE
    <svg width="26" height="14" viewBox="0 0 26 14" aria-hidden="true"><polyline points="2,2 13,12 24,2" fill="none" stroke="#111" stroke-width="2.6"/></svg>
  </div>

  <footer class="site-footer">
    <p class="copyright">Copyright Tobias Wrenholt 2017</p>
    <a class="social" style="left:812px;top:22px" href="https://www.quorvely.com/notes/how-win-court-tobias-wrenholt/"><span class="social-dot"></span><span class="social-name">Quorvely</span></a>
    <a class="social" style="left:812px;top:40px" href="#"><span class="social-dot"></span><span class="social-name">Chirrup</span></a>
  </footer>
</body>
</html>
```